Business card design for IT consulting company

Looking for a simple, modern, clean business card design.
Open to reworking our existing logo.

Attached is our current business cards which we do not like.
Ideally double sided with something simple on the back.
Rectangle / Horizonal only.
No rounded edges on the card.
White as the dominate color is preferred.

Target Market(s)

clients, legal, oil & gas, medical, professionals

Industry/Entity Type

IT, tech, consulting

Contact Information for Business Card

Name, Title, email, phone, cell, website

Font styles to use
Sans Serif

Requirements
Must have
• Clean design
Should not have
• loud colors or unusual fonts, etc

```html
<!DOCTYPE html>
<html lang="en">
<head>
<meta charset="utf-8">
<title>Kestrel – Business Card</title>
<link rel="stylesheet" href="https://fonts.googleapis.com/css2?family=Open+Sans:wght@400;600;700;800&display=swap">
<style>
  :root {
    --stage: #232324;
    --card-dark: #1e1e20;
    --pattern-dark: #2c2c2f;
    --pattern-light: #343438;
    --paper: #ffffff;
    --red: #ee4056;
    --yellow: #fcc52f;
    --navy: #26266e;
    --ink: #1a1a1a;
  }
  * { box-sizing: border-box; margin: 0; padding: 0; }
  html, body {
    width: 1200px; height: 780px; overflow: hidden;
    background: var(--stage);
    font-family: "Open Sans", Arial, sans-serif;
  }
  .stage {
    width: 1200px; height: 780px;
    display: flex; align-items: center; justify-content: center; gap: 30px;
  }

  /* Back of card */
  .card-back {
    position: relative; flex: none;
    width: 470px; height: 270px;
    background: var(--card-dark);
    box-shadow: 0 18px 40px rgba(0,0,0,.55);
    overflow: hidden;
  }
  .card-back__pattern {
    position: absolute; inset: 0;
    background: linear-gradient(135deg, var(--pattern-light), var(--pattern-dark));
  }
  .card-back__band {
    position: absolute; left: 30px; right: 30px; top: 70px; height: 130px;
    background: var(--card-dark);
    display: flex; align-items: center; justify-content: center; gap: 26px;
  }
  .brand-mark { display: flex; flex-direction: column; align-items: center; gap: 6px; }
  .brand-mark__square { width: 48px; height: 48px; background: var(--red); border-radius: 8px; }
  .brand-mark__name { font-weight: 700; font-size: 17px; color: var(--paper); }
  .card-back__tagline { font-weight: 700; font-size: 52px; color: var(--paper); line-height: 1; }

  /* Front of card */
  .card-front {
    flex: none;
    width: 640px; height: 366px;
    background: var(--paper);
    box-shadow: 0 18px 40px rgba(0,0,0,.55);
    display: flex; align-items: center;
  }
  .front-logo {
    width: 250px; height: 100%;
    display: flex; align-items: center; justify-content: center; gap: 12px;
  }
  .front-logo__square { width: 50px; height: 50px; background: var(--red); border-radius: 9px; flex: none; }
  .front-logo__name { font-weight: 700; font-size: 34px; color: var(--navy); }

  .details {
    width: 370px;
    display: flex; flex-direction: column; align-items: center; text-align: center;
  }
  .person__name { font-weight: 800; font-size: 32px; line-height: 1.15; }
  .person__first { color: var(--yellow); }
  .person__last { color: var(--red); }
  .person__title { font-weight: 600; font-size: 14px; color: var(--ink); margin-top: 2px; }

  .dot-row { display: flex; align-items: center; justify-content: center; margin-top: 12px; }
  .dot-row svg { display: block; flex: none; }
  .icon {
    width: 26px; height: 26px; border-radius: 50%;
    background: var(--red);
    display: flex; align-items: center; justify-content: center;
    flex: none; margin: 0 3px;
  }
  .icon svg { width: 15px; height: 15px; }

  .contact { margin-top: 8px; font-size: 16px; line-height: 1.35; color: var(--ink); }
  .website { margin-top: 8px; font-size: 16px; color: var(--ink); }
</style>
</head>
<body>
<main class="stage">

  <section class="card-back">
    <div class="card-back__pattern" role="img" aria-label="Repeating pattern of small embossed brand squares in dark grey"></div>
    <div class="card-back__band">
      <div class="brand-mark">
        <div class="brand-mark__square"></div>
        <span class="brand-mark__name">Kestrel</span>
      </div>
      <span class="card-back__tagline">Solutions</span>
    </div>
  </section>

  <section class="card-front">
    <div class="front-logo">
      <div class="front-logo__square"></div>
      <span class="front-logo__name">Kestrel</span>
    </div>

    <div class="details">
      <div class="person__name"><span class="person__first">Daniel</span> <span class="person__last">Reyes</span></div>
      <div class="person__title">IT Consultant</div>

      <div class="dot-row">
        <div class="icon">
          <svg viewBox="0 0 24 24" fill="#fff"><path d="M6.6 10.8a15 15 0 0 0 6.6 6.6l2.2-2.2c.3-.3.7-.4 1-.2 1.1.4 2.3.6 3.6.6.6 0 1 .4 1 1V20c0 .6-.4 1-1 1A17 17 0 0 1 3 4c0-.6.4-1 1-1h3.5c.6 0 1 .4 1 1 0 1.3.2 2.5.6 3.6.1.3 0 .7-.2 1z"/></svg>
        </div>
        <div class="icon">
          <svg viewBox="0 0 24 24" fill="none" stroke="#fff" stroke-width="2"><rect x="7" y="2" width="10" height="20" rx="2"/><line x1="11" y1="18" x2="13" y2="18"/></svg>
        </div>
        <div class="icon">
          <svg viewBox="0 0 24 24" fill="none" stroke="#fff" stroke-width="2"><rect x="3" y="6" width="18" height="13" rx="1"/><path d="M3 7l9 7 9-7"/></svg>
        </div>
        <svg width="140" height="20" viewBox="0 0 140 20" fill="var(--red)">
          <circle cx="10" cy="10" r="7"/><circle cx="28" cy="10" r="6.3"/><circle cx="45" cy="10" r="5.6"/>
          <circle cx="61" cy="10" r="5"/><circle cx="76" cy="10" r="4.4"/><circle cx="90" cy="10" r="3.8"/>
          <circle cx="103" cy="10" r="3.2"/><circle cx="115" cy="10" r="2.6"/><circle cx="126" cy="10" r="2"/>
        </svg>
      </div>

      <div class="contact">
        <div>(555) 014-2290</div>
        <div>(555) 013-7741</div>
        <div>daniel.reyes@kestrel.ca</div>
      </div>

      <div class="dot-row">
        <svg width="128" height="20" viewBox="0 0 128 20" fill="var(--red)">
          <circle cx="4" cy="10" r="2"/><circle cx="15" cy="10" r="2.6"/><circle cx="27" cy="10" r="3.2"/>
          <circle cx="40" cy="10" r="3.8"/><circle cx="54" cy="10" r="4.4"/><circle cx="69" cy="10" r="5"/>
          <circle cx="85" cy="10" r="5.6"/><circle cx="102" cy="10" r="6.3"/><circle cx="120" cy="10" r="7"/>
        </svg>
        <div class="icon">
          <svg viewBox="0 0 24 24" fill="none" stroke="#fff" stroke-width="2"><circle cx="12" cy="12" r="9"/><path d="M3 12h18M12 3c3 3 3 15 0 18M12 3c-3 3-3 15 0 18"/></svg>
        </div>
        <svg width="128" height="20" viewBox="0 0 128 20" fill="var(--red)">
          <circle cx="8" cy="10" r="7"/><circle cx="26" cy="10" r="6.3"/><circle cx="43" cy="10" r="5.6"/>
          <circle cx="59" cy="10" r="5"/><circle cx="74" cy="10" r="4.4"/><circle cx="88" cy="10" r="3.8"/>
          <circle cx="101" cy="10" r="3.2"/><circle cx="113" cy="10" r="2.6"/><circle cx="124" cy="10" r="2"/>
        </svg>
      </div>

      <div class="website">www.kestrel.ca</div>
    </div>
  </section>

</main>
</body>
</html>
```